Business Card Design for LeafSpire (Farming Devices)

We need Business Cards for our new Company based in Switzerland called "LeafSpire" We develop innovativ products for indoor and outdoor Farming for household and components for vertical farming. Our initial BloomNook gives people the possibility to grow their own food at home all year round. The design should communicate freshness, innovation, health.

```html
<!DOCTYPE html>
<html lang="en">
<head>
<meta charset="utf-8">
<title>LeafSpire Business Card</title>
<link rel="stylesheet" href="https://fonts.googleapis.com/css2?family=Ubuntu:wght@400;500;700&display=swap">
<style>
  :root {
    --backdrop: #c4c8d0;
    --photo-deep: #0d4f8a;
    --photo-mid: #1565a8;
    --photo-leaf: #1f6a5e;
    --leaf-green: #77b441;
    --ink-blue: #0f6db5;
    --ink-green: #2a7a3a;
    --paper: #ffffff;
  }
  * { box-sizing: border-box; margin: 0; padding: 0; }
  html, body {
    width: 1200px; height: 1200px; overflow: hidden;
    background: var(--backdrop);
    font-family: "Ubuntu", sans-serif;
  }
  .card {
    position: absolute; top: 332px;
    width: 320px; height: 578px;
    overflow: hidden;
  }
  .card--front { left: 245px; }
  .card--back { left: 633px; background: var(--paper); }

  .photo {
    position: absolute; inset: 0;
    background:
      radial-gradient(ellipse 60% 40% at 30% 30%, rgba(31,106,94,.55), transparent 70%),
      radial-gradient(ellipse 50% 40% at 75% 70%, rgba(31,106,94,.5), transparent 70%),
      linear-gradient(90deg, var(--photo-deep), var(--photo-mid) 30%, var(--photo-deep) 55%, var(--photo-mid) 80%, var(--photo-deep));
  }
  .card--back .photo { height: 250px; }

  .brand {
    position: absolute; left: 0; right: 0;
    display: flex; align-items: center; justify-content: center; gap: 8px;
    color: var(--paper); font-weight: 500; letter-spacing: .3px;
  }
  .brand__dot {
    width: 12px; height: 12px; border-radius: 50%;
    background: var(--leaf-green);
  }
  .card--front .brand { top: 268px; font-size: 35px; }
  .card--back .brand { top: 76px; font-size: 31px; }

  .stem-art { position: absolute; inset: 0; }

  .person {
    position: absolute; left: 71px; top: 303px;
    color: var(--ink-blue);
  }
  .person__name { font-size: 25px; font-weight: 700; letter-spacing: .3px; }
  .person__title { font-size: 19px; font-weight: 500; margin-top: 4px; }

  .contacts {
    position: absolute; left: 73px; top: 430px;
    list-style: none; color: var(--ink-green);
    font-size: 17px; line-height: 25px; letter-spacing: .3px;
  }
</style>
</head>
<body>

<section class="card card--front">
  <div class="photo" role="img" aria-label="Blue-toned photo of leafy greens growing on vertical farming towers"></div>
  <div class="brand"><span class="brand__dot"></span>LeafSpire</div>
  <svg class="stem-art" viewBox="0 0 320 578" aria-hidden="true">
    <line x1="160" y1="317" x2="160" y2="532" stroke="var(--leaf-green)" stroke-width="3"/>
  </svg>
  <svg class="stem-art" viewBox="0 0 320 578" role="img" aria-label="Root system illustration">
    <ellipse cx="160" cy="545" rx="40" ry="14" fill="var(--leaf-green)" opacity=".45"/>
  </svg>
</section>

<section class="card card--back">
  <div class="photo" role="img" aria-label="Blue-toned photo of leafy greens growing on vertical farming towers"></div>
  <div class="brand"><span class="brand__dot"></span>LeafSpire</div>

  <svg class="stem-art" viewBox="0 0 320 578" aria-hidden="true">
    <path class="arc-band" d="M0 224 C60 120 210 105 290 220 C300 238 308 246 320 246 L320 578 L0 578 Z" fill="var(--leaf-green)"/>
    <path class="arc-paper" d="M0 240 C60 145 200 130 278 230 C290 244 300 248 320 248 L320 578 L0 578 Z" fill="var(--paper)"/>
    <line x1="54" y1="250" x2="54" y2="545" stroke="var(--leaf-green)" stroke-width="3"/>
    <g class="contact-icons" fill="var(--paper)" stroke="var(--leaf-green)" stroke-width="1.6">
      <circle cx="54" cy="440" r="8"/>
      <circle cx="54" cy="440" r="3" fill="none"/>
      <circle cx="54" cy="465" r="8"/>
      <path d="M50 461 q0 8 8 8" fill="none"/>
      <circle cx="54" cy="490" r="8"/>
      <text x="54" y="494.5" font-size="12" font-weight="700" text-anchor="middle" fill="var(--leaf-green)" stroke="none" font-family="Ubuntu, sans-serif">@</text>
      <circle cx="54" cy="515" r="8"/>
      <ellipse cx="54" cy="515" rx="3.5" ry="8" fill="none"/>
      <line x1="46" y1="515" x2="62" y2="515"/>
    </g>
  </svg>
  <svg class="stem-art" viewBox="0 0 320 578" role="img" aria-label="Seedling leaves illustration">
    <ellipse cx="54" cy="245" rx="26" ry="20" fill="var(--leaf-green)" opacity=".45"/>
  </svg>
  <svg class="stem-art" viewBox="0 0 320 578" role="img" aria-label="Root system illustration">
    <ellipse cx="54" cy="556" rx="42" ry="15" fill="var(--leaf-green)" opacity=".45"/>
  </svg>

  <div class="person">
    <p class="person__name">NAME SURNAME</p>
    <p class="person__title">your title</p>
  </div>

  <ul class="contacts">
    <li>your company address</li>
    <li>00 1234 1234</li>
    <li>email@yourcompany.com</li>
    <li>www.yourcompany.com</li>
  </ul>
</section>

</body>
</html>
```